Guarding One's Body Using Sharp Steel Cover

Hi we are producing a self defense course entitled Guarding One's Body Using Sharp Steel: A Complete Manual For Learning The Finest And Handiest Wilderness Tool In Recorded History.

I listed this as a book cover but it will actually be a DVD set, but the book cover model works fine.

See below for design examples - I am thinking we need a cover that will appeal to military/survival type people.

Target Market(s)

survivalists, cops, preppers, gun owners, martial artists, and average people wanting to learn how to defend themselves

Industry/Entity Type

Defense

Requirements
Must have
• Title: GUARDING ONE'S BODY USING SHARP STEEL: A COMPLETE MANUAL FOR LEARNING THE FINEST AND HANDIEST WILDERNESS TOOL IN RECORDED HISTORY
Nice to have
• Please look at these sample designs from other books as a model:
• https://files.plorvexa.org/media/en/4/27/BrindelQXMP.jpg - This stye is ideal.
• Other good examples:
• https://pics2.talvorn.com/8143907_k370.jpg
• http://m.zephquill.com/titles/2719058463k/48071935.jpg
• http://img.crondelmart.com/pics/P/73Tm58QyzFr._BX_KL410_TR316,410_.jpg
• http://3.cdn.wendoplix.net/-RTyZWLMMKAQ/BNWq_hufxaT/BBBBBBBBv8G/DKNp815ZaXW/s1600/Q4710392.JPG

```html
<!DOCTYPE html>
<html lang="en">
<head>
<meta charset="utf-8">
<title>Guarding One's Body Using Sharp Steel – Cover</title>
<link rel="stylesheet" href="https://fonts.googleapis.com/css2?family=Anton&family=Oswald:wght@500&display=swap">
<style>
  :root {
    --stage: #d6d6d6;
    --ink-deep: #0f0b1f;
    --ink-violet: #2a1a3f;
    --ember: #b8321c;
    --glow: #e0702a;
    --shadow-maroon: #3a0a0e;
    --blood: #e8202a;
    --paper: #ffffff;
    --bone: #f1e4d6;
    --author-red: #c8262b;
  }
  * { margin: 0; padding: 0; box-sizing: border-box; }
  html, body { width: 1200px; height: 800px; overflow: hidden; }
  body {
    background: radial-gradient(ellipse at 50% 45%, #e6e6e6 0%, var(--stage) 70%, #bcbcbc 100%);
    position: relative;
  }
  .cover {
    position: absolute;
    left: 360px; top: 40px;
    width: 480px; height: 720px;
    overflow: hidden;
    background: var(--ink-deep);
    box-shadow: 0 12px 30px rgba(0,0,0,.35);
  }
  .cover-texture {
    position: absolute; inset: 0;
    background:
      radial-gradient(ellipse 45% 30% at 18% 30%, rgba(224,112,42,.55), transparent 70%),
      radial-gradient(ellipse 40% 25% at 20% 62%, rgba(224,112,42,.35), transparent 70%),
      radial-gradient(ellipse 35% 30% at 85% 48%, rgba(184,50,28,.30), transparent 70%),
      linear-gradient(160deg, var(--ink-violet) 0%, var(--ink-deep) 55%, #1b1030 100%);
  }
  .cover-figure {
    position: absolute;
    left: 70px; top: 190px;
    width: 360px; height: 530px;
    background:
      radial-gradient(ellipse 24% 20% at 52% 26%, rgba(70,10,14,.95), rgba(58,10,14,.7) 70%, transparent 100%),
      radial-gradient(ellipse 50% 42% at 50% 78%, rgba(58,10,14,.9), rgba(40,8,16,.6) 70%, transparent 100%);
  }
  .rule {
    position: absolute; left: 0; right: 0;
    background: var(--paper);
  }
  .rule-top { top: 18px; height: 5px; }
  .rule-mid { top: 282px; height: 8px; }
  .rule-mid-thin { top: 296px; height: 2px; }
  .title {
    position: absolute; left: 24px; right: 20px; top: 34px;
    font-family: 'Anton', sans-serif;
    font-weight: 400;
    text-transform: uppercase;
    line-height: .95;
  }
  .title-lead {
    display: block;
    color: var(--paper);
    font-size: 46px;
    letter-spacing: .5px;
  }
  .title-key {
    display: block;
    color: var(--blood);
    font-size: 90px;
    line-height: .95;
    margin-top: 6px;
    letter-spacing: -1px;
  }
  .subtitle {
    font-family: 'Anton', sans-serif;
    font-weight: 400;
    color: var(--bone);
    text-transform: uppercase;
  }
  .subtitle-col {
    position: absolute;
    display: flex; flex-direction: column;
    line-height: .98;
  }
  .subtitle-left { left: 26px; top: 440px; }
  .subtitle-right { left: 248px; top: 404px; }
  .subtitle .sm { font-size: 20px; letter-spacing: 1px; }
  .subtitle .md { font-size: 30px; }
  .subtitle .lg { font-size: 50px; }
  .amp {
    position: absolute; left: 184px; top: 510px;
    font-family: 'Anton', sans-serif;
    font-size: 92px; line-height: 1;
    color: var(--author-red);
    opacity: .92;
  }
  .author {
    position: absolute; left: 0; right: 0; bottom: 36px;
    text-align: center;
    font-family: 'Oswald', sans-serif; font-weight: 500;
    font-size: 20px; letter-spacing: 12px;
    color: var(--author-red);
    text-transform: uppercase;
  }
</style>
</head>
<body>
  <main class="cover">
    <div class="cover-texture" role="img" aria-label="Dark grunge background with glowing orange cracks"></div>
    <div class="cover-figure" role="img" aria-label="Shadowed silhouette of a standing figure in dark red"></div>

    <div class="rule rule-top"></div>

    <h1 class="title">
      <span class="title-lead">Guarding One's Body<br>Using</span>
      <span class="title-key">Sharp Steel</span>
    </h1>

    <div class="rule rule-mid"></div>
    <div class="rule rule-mid-thin"></div>

    <h2 class="subtitle">
      <span class="subtitle-col subtitle-left">
        <span class="sm">A Complete</span>
        <span class="lg">Manual</span>
        <span class="sm">For Learning</span>
        <span class="md">The</span>
        <span class="md">Finest</span>
      </span>
      <span class="amp">&amp;</span>
      <span class="subtitle-col subtitle-right">
        <span class="md">Handiest</span>
        <span class="md">Wilderness</span>
        <span class="sm">Tool In Recorded</span>
        <span class="lg">History</span>
      </span>
    </h2>

    <p class="author">Dorian Vasselle</p>
  </main>
</body>
</html>
```